Modern Billboard Ad for Criminal Defense Firm

10.5 x 36 We're looking for something to set us apart from the local competition. Looking for sleek and modern. We're a mid-sized firm in a small market city. We want to give the artist room to be creative on this one.
Thanks

Target Market(s)

Adult clients who have been charged with a crime/DWI

Industry/Entity Type

legal

Font styles to use
Serif
Sans Serif

Requirements
Must have
• Needs to have the firm name in large lettering. Law Offices of Marcus T Whitfield. “PLLC” does not have to be included. Phone number of (555) 384-1927 should be included but not the main focus.
Nice to have
• A call to action or something similar. “Don’t go it alone, call today.”, “ Arrested?”

```html
<!DOCTYPE html>
<html lang="en">
<head>
<meta charset="utf-8">
<title>Law Offices of Marcus T Whitfield – Billboard</title>
<link href="https://fonts.googleapis.com/css2?family=Montserrat:wght@700;800;900&display=swap" rel="stylesheet">
<style>
  :root {
    --navy: #1b3a8c;
    --navy-deep: #132a6b;
    --navy-ink: #163a78;
    --red: #e41d24;
    --white: #ffffff;
    --shadow: #0d1530;
    --page: #e9ecf1;
    --photo-tone: #6b6a66;
    --badge-tone: #1d2330;
  }
  html, body {
    margin: 0;
    padding: 0;
    width: 1200px;
    height: 768px;
    overflow: hidden;
    background: var(--page);
  }
  .billboard {
    position: absolute;
    left: 0;
    top: 209px;
    width: 1200px;
    height: 352px;
    background: var(--white);
    overflow: hidden;
    font-family: "Montserrat", "Arial", sans-serif;
  }
  .brand-panel {
    position: absolute;
    left: 0;
    top: 0;
    width: 698px;
    height: 352px;
    background: linear-gradient(120deg, var(--navy-deep) 0%, var(--navy) 55%, #2448a6 100%);
  }
  .brand-panel svg {
    position: absolute;
    inset: 0;
  }
  .dot-texture {
    position: absolute;
    left: 500px;
    top: 0;
    width: 198px;
    height: 172px;
    background: radial-gradient(ellipse at 85% 55%, rgba(10, 24, 70, 0.55) 0%, rgba(10, 24, 70, 0.25) 45%, rgba(10, 24, 70, 0) 75%);
  }
  .firm-name {
    position: absolute;
    left: 48px;
    top: 34px;
    margin: 0;
    color: var(--white);
    font-weight: 800;
    text-transform: uppercase;
    text-shadow: 4px 4px 0 var(--shadow);
    line-height: 1;
  }
  .firm-name .prefix {
    display: block;
    font-size: 50px;
    letter-spacing: -1.5px;
  }
  .firm-name .attorney {
    display: block;
    margin-top: 4px;
    font-size: 52px;
    letter-spacing: -1.5px;
  }
  .attorney-photo {
    position: absolute;
    left: 48px;
    top: 172px;
    width: 120px;
    height: 143px;
    border: 4px solid var(--white);
    background: linear-gradient(180deg, #5a5a4e 0%, var(--photo-tone) 45%, #8a8e98 100%);
  }
  .award-badge {
    position: absolute;
    left: 192px;
    top: 172px;
    width: 97px;
    height: 143px;
    border: 4px solid var(--white);
    background: var(--badge-tone);
  }
  .headline {
    position: absolute;
    left: 357px;
    top: 170px;
    width: 843px;
    height: 146px;
    background: var(--red);
    box-shadow: 0 7px 0 var(--shadow);
    display: flex;
    align-items: center;
    justify-content: center;
  }
  .headline span {
    color: var(--white);
    font-weight: 900;
    font-size: 118px;
    letter-spacing: -3px;
    text-shadow: 6px 6px 0 #8e1016;
    line-height: 1;
    padding-top: 6px;
  }
  .call-block {
    position: absolute;
    left: 698px;
    top: 0;
    width: 502px;
    height: 170px;
    text-align: center;
  }
  .call-to-action {
    margin: 28px 0 0;
    color: var(--red);
    font-weight: 800;
    font-size: 29px;
    line-height: 31px;
    text-transform: uppercase;
  }
  .call-to-action .rule-line {
    display: inline-flex;
    align-items: center;
    gap: 10px;
  }
  .call-to-action .rule-line::before,
  .call-to-action .rule-line::after {
    content: "";
    width: 46px;
    height: 2px;
    background: var(--navy-ink);
  }
  .phone {
    margin: 0;
    color: var(--navy-ink);
    font-weight: 800;
    font-size: 56px;
    letter-spacing: -1px;
    line-height: 48px;
  }
</style>
</head>
<body>
  <section class="billboard">
    <div class="brand-panel">
      <svg width="698" height="352" viewBox="0 0 698 352" aria-hidden="true">
        <polygon points="470,0 698,0 698,352 600,352" fill="#2a52b5" opacity="0.45"/>
        <polygon points="560,0 698,0 698,170 640,170" fill="#11245e" opacity="0.35"/>
        <polygon points="380,352 470,332 698,300 698,352" fill="#2d5bc4" opacity="0.35"/>
      </svg>
      <div class="dot-texture" role="img" aria-label="Halftone dot texture"></div>
      <h1 class="firm-name">
        <span class="prefix">Law Offices of</span>
        <span class="attorney">Marcus T Whitfield</span>
      </h1>
      <div class="attorney-photo" role="img" aria-label="Portrait of the attorney"></div>
      <div class="award-badge" role="img" aria-label="Community award badge"></div>
    </div>

    <div class="call-block">
      <p class="call-to-action">Don’t go it alone,<br><span class="rule-line">Call today</span></p>
      <p class="phone">(555) 384-1927</p>
    </div>

    <div class="headline"><span>ARRESTED?</span></div>
  </section>
</body>
</html>
```